Doctor in Veterinary Medecine/ veterinarian

I am a vet and would like a buisness card which is simple yet elegant and professional.
My aim is to help as much animals as I can. My main field of expertise are dogs and cats. I would like the card to reflect a "family doctor" feeling.
It should not be the traditional picture of a paw or a dog but yet it should have a sign of a pet on it. I would like to have my name Lina Haddour as well as my profession D.V.M and my number.

Target Market(s)

Lebanese population who have pets

Industry/Entity Type

Doctor

Contact Information for Business Card

Should contain my profession " D.V.M", my full name "Lina Haddour" and my number "0096171552934"

Requirements
Must have
• A certain picture depicting my profession
Nice to have
• Some sort of picture related to pets and animals
Should not have
• A picture of a paw or a dog. I need something more creative

```html
<!DOCTYPE html>
<html lang="en">
<head>
<meta charset="utf-8">
<title>Lina Haddour — Veterinary Medicine Business Card</title>
<link href="https://fonts.googleapis.com/css2?family=Baumans&family=Open+Sans:wght@400;700&display=swap" rel="stylesheet">
<style>
  :root {
    --page-bg: #ececec;
    --card-bg: #ffffff;
    --brand-blue: #1a8fd0;
    --text-dark: #333333;
    --text-mid: #444444;
    --art-grey: #d6d9dc;
    --art-blue: #bfe0f2;
  }
  html, body {
    margin: 0;
    padding: 0;
    width: 1200px;
    height: 848px;
    overflow: hidden;
    background: var(--page-bg);
  }
  .business-card {
    position: absolute;
    left: 50px;
    top: 96px;
    width: 1100px;
    height: 655px;
    background: var(--card-bg);
    overflow: hidden;
    box-shadow: 0 0 0 1px #e2e2e2;
  }
  .mascot-illustration {
    position: absolute;
    left: 73px;
    top: 65px;
    width: 285px;
    height: 543px;
    border-radius: 40px;
    background: linear-gradient(180deg, var(--art-grey) 0%, #e9ebed 45%, var(--art-blue) 100%);
  }
  .specialty-title {
    position: absolute;
    left: 392px;
    top: 274px;
    width: 640px;
    margin: 0;
    font-family: "Baumans", "Comfortaa", sans-serif;
    font-weight: 400;
    font-size: 40px;
    line-height: 1;
    letter-spacing: 3px;
    text-transform: uppercase;
    color: var(--brand-blue);
    white-space: nowrap;
  }
  .vet-identity {
    position: absolute;
    left: 546px;
    top: 372px;
    width: 300px;
    text-align: center;
    font-family: "Open Sans", Arial, sans-serif;
    color: var(--text-dark);
  }
  .vet-name {
    margin: 0;
    font-size: 30px;
    font-weight: 700;
    line-height: 44px;
  }
  .vet-degree {
    margin: 0;
    font-size: 28px;
    font-weight: 400;
    line-height: 40px;
    color: var(--text-mid);
  }
  .vet-phone {
    position: absolute;
    left: 516px;
    top: 486px;
    display: flex;
    align-items: center;
    gap: 16px;
    font-family: "Open Sans", Arial, sans-serif;
    font-size: 38px;
    color: var(--text-dark);
  }
  .phone-icon { width: 30px; height: 44px; }
  .corner-badge {
    position: absolute;
    right: 0;
    bottom: 0;
    width: 190px;
    height: 190px;
  }
</style>
</head>
<body>
  <main class="business-card">
    <div class="mascot-illustration" role="img" aria-label="Illustration of a cartoon cat veterinarian wearing blue glasses, a white coat and a blue stethoscope"></div>

    <h1 class="specialty-title">Veterinary Medicine</h1>

    <div class="vet-identity">
      <p class="vet-name">Lina Haddour</p>
      <p class="vet-degree">D.V.M</p>
    </div>

    <div class="vet-phone">
      <svg class="phone-icon" viewBox="0 0 30 44" aria-hidden="true">
        <rect x="2" y="2" width="26" height="40" rx="4" fill="none" stroke="var(--brand-blue)" stroke-width="3"/>
        <rect x="6" y="8" width="18" height="24" fill="var(--brand-blue)" opacity="0.25"/>
        <rect x="11" y="35" width="8" height="3" rx="1.5" fill="var(--brand-blue)"/>
      </svg>
      <span>0096171552934</span>
    </div>

    <svg class="corner-badge" viewBox="0 0 190 190" aria-hidden="true">
      <polygon points="190,0 190,190 0,190" fill="var(--brand-blue)"/>
      <rect x="125" y="103" width="22" height="66" fill="#ffffff"/>
      <rect x="103" y="125" width="66" height="22" fill="#ffffff"/>
    </svg>
  </main>
</body>
</html>
```